TQ Regulatory Partners - Biz Card - Re-do

I would like a re-do on my business card.

See my Internet site - tqregpartners.com

1) Remove direct phone line.
2) Add company moto - integrity, diligence, and excellence
3) Add Consulting Services listing:
-Benefit Technology
-ERISA Compliance
-Contract/Vendor Management
-Human Resource/Payroll
-Medical/Prescription Drug
-Integrated Leave of Absence

Target Market(s)

Employee benefit consulting and insurance purchasers, Usually human resource executives

Industry/Entity Type

Human Resource

Contact Information for Business Card

Same business card color scheme, logo,

Font styles to use
Sans Serif

Requirements
Must have
• Same color scheme and logo. Remove direct phone number. Keep all numbers, internet address.

```html
<!DOCTYPE html>
<html lang="en">
<head>
<meta charset="utf-8">
<title>TQ Regulatory Partners – Business Card</title>
<link rel="stylesheet" href="https://fonts.googleapis.com/css2?family=Lato:wght@400;700&family=Tinos:wght@700&display=swap">
<style>
  :root {
    --backdrop: #e9e4dd;
    --card-light: #dcbb93;
    --card-mid: #c9a276;
    --card-dark: #b98d60;
    --ink: #14100c;
    --card-shadow: rgba(40, 25, 10, 0.35);
  }
  * { margin: 0; padding: 0; box-sizing: border-box; }
  html, body { width: 1200px; height: 900px; overflow: hidden; }
  body {
    position: relative;
    background: var(--backdrop);
    font-family: "Lato", Arial, sans-serif;
    color: var(--ink);
  }
  .card {
    position: absolute;
    width: 556px;
    height: 343px;
    background: linear-gradient(160deg, var(--card-light) 0%, var(--card-mid) 50%, var(--card-dark) 100%);
    box-shadow: 3px 4px 8px var(--card-shadow);
  }
  .card--front { left: 330px; top: 90px; }
  .card--back { left: 330px; top: 470px; }

  .front-content {
    position: absolute;
    left: 0; right: 0; top: 53px;
    text-align: center;
  }
  .person-name {
    font-family: "Tinos", "Times New Roman", serif;
    font-weight: 700;
    font-size: 23px;
    line-height: 26px;
  }
  .person-title { font-size: 15px; line-height: 17px; }
  .divider {
    width: 206px;
    height: 1px;
    background: var(--ink);
    margin: 6px auto 6px;
  }
  .contact-block { font-size: 15px; line-height: 20px; }
  .contact-label { font-weight: 700; }
  .services { font-size: 15px; line-height: 20px; margin-top: 2px; }
  .service-dot {
    display: inline-block;
    width: 8px; height: 8px;
    border-radius: 50%;
    background: var(--ink);
    margin: 0 5px 2px;
    vertical-align: middle;
  }

  .brand {
    position: absolute;
    left: 116px; top: 99px;
    display: flex;
    align-items: center;
    gap: 20px;
  }
  .brand-mark {
    width: 112px; height: 112px;
    border-radius: 50%;
    background: var(--ink);
  }
  .brand-name {
    font-size: 31px;
    line-height: 40px;
    font-weight: 400;
  }
  .motto {
    position: absolute;
    left: 0; right: 0; top: 225px;
    text-align: center;
    font-size: 16px;
    letter-spacing: 0.3px;
  }
</style>
</head>
<body>
  <section class="card card--front">
    <div class="front-content">
      <div class="person-name">Dana Marlowe</div>
      <div class="person-title">President</div>
      <div class="divider"></div>
      <div class="contact-block">
        <div><span class="contact-label">P:</span> 555.210.4810 | <span class="contact-label">F:</span> 555.210.4811</div>
        <div>dmarlowe@tqregpartners.com</div>
        <div>www.tqregpartners</div>
      </div>
      <div class="divider"></div>
      <div class="contact-block">
        <div>118 Harbor Street NW, Suite 300</div>
        <div>Lakeview, MI 49010</div>
      </div>
      <div class="divider"></div>
      <div class="services">
        <div>Benefit Technology<span class="service-dot"></span>ERISA Compliance</div>
        <div>Human Resource/Payroll<span class="service-dot"></span>Medical/Prescription Drug</div>
        <div>Contract/Vendor Management<span class="service-dot"></span>Integrated Leave of Absence</div>
      </div>
    </div>
  </section>

  <section class="card card--back">
    <div class="brand">
      <div class="brand-mark"></div>
      <div class="brand-name">TQ Regulatory<br>Partners</div>
    </div>
    <div class="motto">INTEGRITY, DILIGENCE AND EXCELLENCE</div>
  </section>
</body>
</html>
```